A UK based Lettings and Property Management Company - Maple Crest Property

Maple Crest Property rents and manages properties on behalf of owners in Liverpool, UK. We are looking for a clean, fresh modern design which incororates our logo.

In terms of pages we initially require:

Home
Lettings
Property Management
Landlords
Tenants
About
Contact

In would like to use colours compatible with the logo

Target Market(s)

People looking to rent property
Owners looking to use our services to let their property

Industry/Entity Type

Property

Contact Information for Business Card

Logo prominent on one side
Address to be edited by us as we are moving premises in October
Name Gavin Holloway
Tel number 0151 486 2037
e-mail gavin@maplecrestproperty.co.uk

Font styles to use
Sans Serif

Colors

Designer to choose colors to be used in the design.

Requirements
Must have
• Clean lines
• Fresh
• Easy navigation
• Easy editing
• Data capture

```html
<!DOCTYPE html>
<html lang="en">
<head>
<meta charset="utf-8">
<title>Maple Crest Property</title>
<link href="https://fonts.googleapis.com/css2?family=Mulish:wght@400;600;700;800&display=swap" rel="stylesheet">
<style>
:root{
  --blue:#4b86db;
  --navy:#161b46;
  --ink:#222;
  --muted:#666;
  --light:#eceeed;
  --beige:#efe6d3;
  --dark-card:#333;
  --card-grey:#ececec;
  --green:#3a9a3a;
  --white:#fff;
}
*{box-sizing:border-box;margin:0;padding:0}
html,body{width:1200px;height:3051px;overflow:hidden}
body{position:relative;background:var(--white);font-family:"Mulish",sans-serif;color:var(--ink)}
.abs{position:absolute}

/* header */
.site-header{left:0;top:0;width:1200px;height:100px;background:var(--light)}
.brand{left:100px;top:26px;display:flex;align-items:center;gap:12px}
.brand-square{width:46px;height:46px;background:var(--navy)}
.brand-name{font-weight:800;font-size:25px;color:var(--navy);line-height:1;letter-spacing:.5px}
.call{right:120px;top:26px;font-size:14px;font-weight:700;color:var(--ink)}
.call span{color:var(--blue)}
.nav{left:444px;top:58px;display:flex;gap:36px;font-size:12.5px;color:var(--ink)}
.nav .active{color:var(--blue)}

/* hero */
.hero{left:0;top:100px;width:1200px;height:486px;background:linear-gradient(180deg,#6c7075 0%,#54534f 45%,#3f3b34 80%,#5e5848 100%)}
.hero-title{left:0;top:270px;width:1200px;text-align:center;font-size:41px;font-weight:700;color:var(--white);letter-spacing:1px}
.hero-sub{left:0;top:323px;width:1200px;text-align:center;font-size:18px;color:var(--white);letter-spacing:1px}
.btn-blue{left:533px;top:376px;width:134px;height:33px;background:var(--blue);color:var(--white);font-size:13px;display:flex;align-items:center;justify-content:center}
.hero-arrow{top:327px;width:34px;height:34px;border-radius:50%;display:flex;align-items:center;justify-content:center}

/* intro */
.intro-mark{left:128px;top:655px;width:55px;height:55px;background:var(--navy)}
.intro-title{left:127px;top:722px;font-size:26px;font-weight:600;color:var(--navy)}
.intro-title span{color:var(--blue)}
.intro-text{left:128px;top:764px;width:465px;font-size:14.5px;line-height:20px;color:#444}
.btn-outline{left:126px;top:868px;width:138px;height:33px;border:2px solid #9db8e2;font-size:13px;display:flex;align-items:center;justify-content:center;color:var(--ink)}
.frame-top{left:805px;top:645px;width:275px;height:220px;background:var(--blue)}
.frame-bottom{left:660px;top:690px;width:275px;height:220px;background:var(--blue)}
.intro-photo{left:668px;top:651px;width:405px;height:252px;background:linear-gradient(180deg,#aebfd2 0%,#dfe4e7 45%,#8e9a86 75%,#5f8a3e 100%)}

/* section headings */
.section-title{left:0;width:1200px;text-align:center;font-size:25px;font-weight:700;color:var(--navy)}

/* services */
.band{left:0;top:1033px;width:1200px;height:364px;background:var(--beige)}
.service{width:314px;height:364px;top:1033px;background:var(--dark-card);color:var(--white)}
.service.featured{top:1023px;height:374px;background:var(--blue)}
.service-head{height:57px;display:flex;align-items:center;justify-content:center;font-size:16px;font-weight:600}
.service.featured .service-head{height:67px}
.service-photo{height:171px}
.service-text{padding:10px 26px 0;text-align:center;font-size:12.5px;line-height:17px}
.more{width:52px;height:52px;border-radius:50%;background:var(--blue);color:var(--white);font-size:13px;display:flex;align-items:center;justify-content:center;top:1369px}
.more.dark{background:var(--navy)}

/* listings */
.listing{top:1554px;width:299px;height:338px;background:var(--card-grey);box-shadow:0 2px 6px rgba(0,0,0,.12)}
.listing-photo{height:171px;position:relative}
.badge{position:absolute;left:0;bottom:-10px;background:var(--green);color:var(--white);font-size:10px;font-weight:700;padding:4px 12px}
.listing-body{padding:16px 26px 0}
.listing-type{font-size:11px;color:#444}
.listing-name{font-size:16px;font-weight:700;color:var(--ink);margin-top:8px}
.listing-loc{font-size:12px;color:#666}
.listing-price{font-size:17px;font-weight:700;color:var(--blue);margin-top:16px;padding-bottom:16px;border-bottom:1px solid #d4d4d4}
.listing-meta{font-size:11px;color:#555;margin-top:14px}

/* testimonials */
.avatar-ring{width:160px;height:160px;border-radius:50%;border:3px solid #e8e8e8;top:2007px;display:flex;align-items:center;justify-content:center}
.avatar{width:136px;height:136px;border-radius:50%}
.t-name{top:2162px;font-size:14px;color:var(--ink)}
.t-name span{color:#999}
.t-text{top:2194px;width:330px;font-size:13.5px;line-height:20px;color:#666}
.stars{top:2276px;display:flex;gap:3px}

/* contact */
.grey-band{left:0;top:2359px;width:1200px;height:306px;background:var(--light)}
.contact-left{left:126px;top:2429px;width:542px;height:474px;background:linear-gradient(135deg,#4b4b4b 0%,#3c3a38 60%,#2e2c2a 100%)}
.contact-right{left:668px;top:2429px;width:404px;height:474px;background:linear-gradient(160deg,#5a78ad 0%,#4b68a0 100%)}
.strip{left:126px;top:2543px;width:26px;height:360px;background:var(--blue)}
.form-title{left:207px;top:2490px;font-size:27px;color:var(--white)}
.form-rule{left:183px;top:2543px;width:214px;height:1px;background:#9a9a9a}
.field{left:207px;width:405px;height:33px;background:#f3f3f3;font-size:11.5px;color:#999;padding:9px 16px}
.send{left:550px;top:2816px;width:38px;height:38px;border-radius:50%;background:var(--blue);display:flex;align-items:center;justify-content:center}
.info{left:718px;color:var(--white)}
.info-title{top:2498px;font-size:20px}
.info-text{font-size:14.5px;line-height:21px}
.info-phone{font-size:21px}
.social{top:2816px;width:36px;height:36px;border-radius:50%;border:1px solid rgba(255,255,255,.7);display:flex;align-items:center;justify-content:center;color:var(--white);font-size:12px;font-weight:700}
.social.on{background:var(--blue);border-color:var(--blue)}

.footer-note{left:182px;top:2964px;font-size:14px;color:#555}
</style>
</head>
<body>

<header class="site-header abs">
  <div class="brand abs"><div class="brand-square"></div><div class="brand-name">Maple Crest Property</div></div>
  <div class="call abs"><span>Call Us:</span> 0151 - 486 - 2037</div>
  <nav class="nav abs">
    <span class="active">Home</span><span>About Us</span><span>Lettings</span><span>Property Management</span><span>Landlords</span><span>Tenants</span><span>Contact</span>
  </nav>
</header>

<section>
  <div class="hero abs" role="img" aria-label="Photograph of a suburban house with a garage under an overcast sky"></div>
  <h1 class="hero-title abs">Maple Crest Property</h1>
  <p class="hero-sub abs">Rents and Manages Properties</p>
  <div class="btn-blue abs">Contact Us &raquo;</div>
  <div class="hero-arrow abs" style="left:34px;background:#fff">
    <svg width="14" height="10" viewBox="0 0 14 10"><path d="M13 5H2M5 1L1 5l4 4" stroke="#333" stroke-width="1.6" fill="none"/></svg>
  </div>
  <div class="hero-arrow abs" style="left:1130px;background:var(--blue)">
    <svg width="14" height="10" viewBox="0 0 14 10"><path d="M1 5h11M9 1l4 4-4 4" stroke="#fff" stroke-width="1.6" fill="none"/></svg>
  </div>
</section>

<section>
  <div class="intro-mark abs"></div>
  <h2 class="intro-title abs">Maple Crest <span>Property</span></h2>
  <p class="intro-text abs">There are many variations of passages of Lorem Ipsum available, but the majority have suffered alteration in some form, by injected humour, or randomised words which don't look even slightly believable. If you are going to use a passage...</p>
  <div class="btn-outline abs">Discover More &raquo;</div>
  <div class="frame-top abs"></div>
  <div class="frame-bottom abs"></div>
  <div class="intro-photo abs" role="img" aria-label="Photograph of a modern apartment building with a lawn"></div>
</section>

<section>
  <h2 class="section-title abs" style="top:963px">What We Do</h2>
  <div class="band abs"></div>
  <article class="service abs" style="left:128px">
    <div class="service-head">Lettings</div>
    <div class="service-photo" role="img" aria-label="Photograph of house keys with a small house keyring" style="background:linear-gradient(135deg,#c99a63,#e8d2b4 55%,#a8743f)"></div>
    <p class="service-text">It is a long established fact that a reader will be distracted by the readable content of a page when looking more-or-less normal...</p>
  </article>
  <article class="service featured abs" style="left:443px">
    <div class="service-head">Property Management</div>
    <div class="service-photo" role="img" aria-label="Photograph of a business handshake over documents" style="background:linear-gradient(135deg,#cfd7e2,#f2f4f7 50%,#9aa7b8)"></div>
    <p class="service-text">It is a long established fact that a reader will be distracted by the readable content of a page when looking more-or-less normal...</p>
  </article>
  <article class="service abs" style="left:759px">
    <div class="service-head">Landlords</div>
    <div class="service-photo" role="img" aria-label="Photograph of hands sheltering a small model house" style="background:linear-gradient(180deg,#f4f4f4,#e6d8cb 60%,#d8b59a)"></div>
    <p class="service-text">It is a long established fact that a reader will be distracted by the readable content of a page when looking more-or-less normal...</p>
  </article>
  <div class="more abs" style="left:258px">More</div>
  <div class="more dark abs" style="left:574px">
    <svg width="14" height="10" viewBox="0 0 14 10"><path d="M1 5h11M9 1l4 4-4 4" stroke="#fff" stroke-width="1.8" fill="none"/></svg>
  </div>
  <div class="more abs" style="left:889px">More</div>
</section>

<section>
  <h2 class="section-title abs" style="top:1494px">Property Listings</h2>
  <svg class="abs" style="left:68px;top:1712px" width="32" height="26" viewBox="0 0 32 26"><path d="M31 13H2M13 1L1 13l12 12" stroke="#999" stroke-width="1.6" fill="none"/></svg>
  <svg class="abs" style="left:1098px;top:1712px" width="32" height="26" viewBox="0 0 32 26"><path d="M1 13h29M19 1l12 12-12 12" stroke="var(--blue)" stroke-width="1.6" fill="none"/></svg>

  <article class="listing abs" style="left:126px">
    <div class="listing-photo" role="img" aria-label="Photograph of a modern house with a pool at dusk" style="background:linear-gradient(180deg,#b9cde0,#e9e3d6 55%,#5b8fb0)"><span class="badge">RENT</span></div>
    <div class="listing-body">
      <div class="listing-type">House</div>
      <div class="listing-name">Lifestyle or Holiday Home</div>
      <div class="listing-loc">(Aigburth UK 2076 )</div>
      <div class="listing-price">Price: $10,000.00</div>
      <div class="listing-meta">2500Sq ft &nbsp;/&nbsp; 4 Bedroom &nbsp;/&nbsp; 3 Bath</div>
    </div>
  </article>
  <article class="listing abs" style="left:450px">
    <div class="listing-photo" role="img" aria-label="Photograph of a multi-storey apartment block" style="background:linear-gradient(180deg,#3e7fc4,#9ab8d4 50%,#7b8676)"><span class="badge">RENT</span></div>
    <div class="listing-body">
      <div class="listing-type">Villa</div>
      <div class="listing-name">Freedom, Space &amp; Solitude</div>
      <div class="listing-loc">(Aigburth UK 2076 )</div>
      <div class="listing-price">Price: $10,000.00</div>
      <div class="listing-meta">2500Sq ft &nbsp;/&nbsp; 4 Bedroom &nbsp;/&nbsp; 3 Bath</div>
    </div>
  </article>
  <article class="listing abs" style="left:775px">
    <div class="listing-photo" role="img" aria-label="Photograph of a large family house lit at twilight" style="background:linear-gradient(180deg,#8e86c9,#b7a9d6 45%,#5d5a6a 75%,#4f6a3a)"><span class="badge">RENT</span></div>
    <div class="listing-body">
      <div class="listing-type">Family Home</div>
      <div class="listing-name">Lifestyle or Holiday Home</div>
      <div class="listing-loc">(Aigburth UK 2076 )</div>
      <div class="listing-price">Price: $50,000.00</div>
      <div class="listing-meta">2500Sq ft &nbsp;/&nbsp; 4 Bedroom &nbsp;/&nbsp; 3 Bath</div>
    </div>
  </article>
</section>

<section>
  <h2 class="section-title abs" style="top:1955px">Testimonials</h2>
  <svg class="abs" style="left:128px;top:2152px" width="22" height="44" viewBox="0 0 22 44"><path d="M21 1L1 22l20 21" stroke="#999" stroke-width="1.6" fill="none"/></svg>
  <svg class="abs" style="left:1050px;top:2152px" width="22" height="44" viewBox="0 0 22 44"><path d="M1 1l20 21L1 43" stroke="var(--blue)" stroke-width="2" fill="none"/></svg>

  <div class="avatar-ring abs" style="left:209px"><div class="avatar" role="img" aria-label="Portrait photo of a client" style="background:linear-gradient(180deg,#c7ccd2,#6f7f99)"></div></div>
  <div class="t-name abs" style="left:208px">Maren T. <span>/ Distribution</span></div>
  <p class="t-text abs" style="left:208px">Contrary to popular belief, Lorem Ipsum is not simply random text. It has roots in a piece of classical Latin literature from 45 BC, making it over...</p>
  <svg class="stars abs" style="left:208px" width="90" height="16" viewBox="0 0 90 16">
    <g fill="var(--green)"><path id="st" d="M8 1l2.2 4.6 5 .7-3.6 3.5.9 5L8 12.4 3.5 14.8l.9-5L.8 6.3l5-.7z"/><use href="#st" x="18"/><use href="#st" x="36"/></g>
    <use href="#st" x="54" fill="none" stroke="var(--green)"/><use href="#st" x="72" fill="none" stroke="var(--green)"/>
  </svg>

  <div class="avatar-ring abs" style="left:670px"><div class="avatar" role="img" aria-label="Portrait photo of a client" style="background:linear-gradient(180deg,#eeeae6,#c9b39c)"></div></div>
  <div class="t-name abs" style="left:669px">Lorna B. <span>/ Distribution</span></div>
  <p class="t-text abs" style="left:669px">Contrary to popular belief, Lorem Ipsum is not simply random text. It has roots in a piece of classical Latin literature from 45 BC, making it over...</p>
  <svg class="stars abs" style="left:669px" width="90" height="16" viewBox="0 0 90 16">
    <g fill="var(--green)"><use href="#st"/><use href="#st" x="18"/><use href="#st" x="36"/></g>
    <use href="#st" x="54" fill="none" stroke="var(--green)"/><use href="#st" x="72" fill="none" stroke="var(--green)"/>
  </svg>
</section>

<section>
  <div class="grey-band abs"></div>
  <div class="contact-left abs" role="img" aria-label="Darkened photograph of an apartment building"></div>
  <div class="contact-right abs" role="img" aria-label="Blue-tinted photograph of a building facade"></div>
  <div class="strip abs"></div>

  <h2 class="form-title abs">Send us a Message</h2>
  <div class="form-rule abs"></div>
  <div class="field abs" style="top:2579px">Your Name</div>
  <div class="field abs" style="top:2630px">Enter your Email</div>
  <div class="field abs" style="top:2681px">Phone</div>
  <div class="field abs" style="top:2732px;height:102px">Type your Message</div>
  <div class="send abs">
    <svg width="16" height="16" viewBox="0 0 16 16"><path d="M1 8l14-6-5 13-2-5z" fill="#fff"/></svg>
  </div>

  <h3 class="info info-title abs">Contact Info</h3>
  <p class="info info-text abs" style="top:2575px">Maple Crest Property<br>48 Harbour View Road,<br>Liverpool, L3 4BQ</p>
  <p class="info info-text abs" style="top:2660px">Phone:</p>
  <p class="info info-phone abs" style="top:2680px">0151 - 486 - 2037</p>
  <p class="info info-text abs" style="top:2726px">Email:<br><u>info@maplecrestproperty.com</u></p>
  <div class="social on abs" style="left:718px">f</div>
  <div class="social abs" style="left:761px">t</div>
  <div class="social abs" style="left:804px">in</div>
</section>

<footer>
  <p class="footer-note abs">2017 &copy; Maple Crest Property All rights reserved.</p>
  <svg class="abs" style="left:1002px;top:2965px" width="14" height="16" viewBox="0 0 14 16"><path d="M7 15V2M2 7l5-5 5 5" stroke="var(--blue)" stroke-width="2" fill="none"/></svg>
</footer>

</body>
</html>
```